A weight loss and fitness website design

I am into different types of modern weight loss techniques for people who are a little fatty and wish to be physically and mentally fit. Basically, the website is to teach people how to reduce weight using different methods such as diet, exercises, yoga and other forms. I would need an eye catching website which would make visitors want to come back. The will be also be different forms of exercises for a health and fit life. This said, my website is to have two categories of
1) weight loss techniques
2) exercise of fit and healthy living.
I prefer bright colors such as green, blue, yellow, and orange. Imagery should include before and after pictures of people suffering from obesity, people under going exercises.
Designers can get ideas and inspiration from the website fitmerlo.com which i was previously part of the team.
Target Market(s)
My target audience are people suffering from obesity, malnutrition and physical deficiency.
Industry/Entity Type
Fitness
Coding
Coded - Design and coding required
Number of Pages Required
1 page
Look and feel

```html
<!DOCTYPE html>
<html lang="en">
<head>
<meta charset="utf-8">
<title>FitNova – Fitness Is A Way Of Life</title>
<link rel="stylesheet" href="https://fonts.googleapis.com/css2?family=Raleway:wght@400;500;600;700&family=Open+Sans:wght@400;600&family=Satisfy&display=swap">
<style>
:root{
  --blue:#1e8fd6;
  --blue-dark:#16639b;
  --sky:#2a9fe0;
  --green:#8cc63f;
  --green-dark:#6ea52a;
  --orange:#f7941d;
  --ink:#333;
  --muted:#666;
  --pale:#eef2ee;
  --pale-blue:#eaf4fb;
  --navy:#0f1c2b;
  --red:#d8262f;
}
*{box-sizing:border-box;margin:0;padding:0}
html,body{width:1200px;height:4839px;overflow:hidden}
body{position:relative;background:#fff;font-family:'Open Sans',Arial,sans-serif;color:var(--ink)}
.abs{position:absolute}
.ph{position:absolute}
h2,h3{font-family:'Raleway',Arial,sans-serif;font-weight:500}
p.copy{font-size:13px;line-height:20px;color:var(--muted)}

/* nav */
.nav{position:absolute;left:0;top:0;width:1200px;height:97px;background:#fff;border-bottom:1px solid #e6e6e6}
.nav-item{position:absolute;top:0;width:120px;margin-left:-60px;text-align:center;font-family:'Raleway',sans-serif;font-size:15px;color:#555;padding-top:18px;white-space:nowrap}
.nav-item.wide{width:170px;margin-left:-85px}
.nav-item svg{display:block;margin:0 auto 6px}
.nav-item.active{width:112px;margin-left:-56px;height:92px;background:var(--blue);color:#fff;border-radius:0 0 56px 56px}

/* logo */
.brand{position:absolute;left:0;top:140px;width:1200px;text-align:center}
.brand-name{font-family:'Raleway',sans-serif;font-weight:500;font-size:96px;color:var(--green);display:inline-flex;align-items:center;gap:22px}
.brand-name i{display:inline-block;width:100px;height:100px;border-radius:50%;background:var(--blue)}

/* subscribe */
.subscribe{position:absolute;left:0;top:387px;width:1200px;height:110px;background:#f4f6f8}
.subscribe .tag{position:absolute;left:80px;top:22px;width:300px;font-family:'Satisfy',cursive;font-size:20px;line-height:26px;color:var(--blue)}
.subscribe label{position:absolute;left:370px;top:36px;font-size:14px}
.subscribe .field{position:absolute;left:472px;top:30px;width:280px;height:34px;background:#fff;border:1px solid #ccc}
.subscribe .btn{position:absolute;left:752px;top:30px;width:120px;height:34px;background:var(--blue);color:#fff;font-size:14px;text-align:center;line-height:34px}
.social{position:absolute;top:30px;width:36px;height:36px;border-radius:50%;background:var(--blue)}
.crowd{position:absolute;left:0;top:497px;width:1200px;height:38px;background:linear-gradient(90deg,#f3c34a,#6fb8e8,#e87c5a,#8cc63f,#f3c34a,#6fb8e8,#e87c5a)}

/* hero */
.hero{position:absolute;left:0;top:535px;width:1200px;height:546px;background:linear-gradient(180deg,#fbe3a8 0%,#f6c878 35%,#f2b464 60%,#5f86a6 74%,#c9b38e 100%)}
.hero h1{position:absolute;left:523px;top:212px;font-family:'Raleway',sans-serif;font-weight:600;font-size:38px;line-height:50px;color:var(--sky);text-shadow:0 1px 2px rgba(255,255,255,.6)}
.hero .cta{position:absolute;left:523px;top:345px;width:240px;height:48px;background:var(--orange);color:#fff;font-family:'Raleway',sans-serif;font-size:20px;text-align:center;line-height:48px}

/* fit */
.fit h2{position:absolute;left:0;top:1140px;width:1200px;text-align:center;font-size:34px;color:var(--blue-dark);font-weight:500}
.fit .lead{position:absolute;left:120px;top:1210px;width:960px;text-align:center}
.card{position:absolute;top:1290px;width:330px;height:205px;background:linear-gradient(90deg,#8a7a6a 0%,#4b9ed6 55%,#2b86c8 100%)}
.card h3{position:absolute;right:14px;top:24px;width:180px;text-align:right;font-size:28px;line-height:30px;color:#fff}
.card p{position:absolute;right:14px;top:92px;width:180px;font-size:11px;line-height:15px;color:#fff}
.card .more{position:absolute;right:20px;bottom:22px;padding:4px 12px;background:var(--green);color:#fff;font-size:11px}

/* feature rows */
.feature h2{position:absolute;font-size:26px;color:#333;text-transform:uppercase}
.feature p.copy{position:absolute;width:500px}
.calendar{position:absolute;left:613px;top:1877px;width:474px;height:349px;background:#f1f1f1}
.calendar .title{position:absolute;left:28px;top:22px;font-family:'Raleway',sans-serif;font-size:44px;color:var(--blue)}
.calendar .title span{color:var(--green)}
.calendar table{position:absolute;left:20px;top:110px;width:430px;border-collapse:collapse;font-size:18px;color:#666;text-align:left}
.calendar th{font-weight:400;color:#555;border-bottom:1px solid #ccc;padding:4px 6px}
.calendar td{padding:9px 6px}
.calendar .sun{color:var(--red)}
.progress-band{position:absolute;left:0;top:2275px;width:1200px;height:677px;background:var(--pale)}
.diet-band{position:absolute;left:0;top:3613px;width:1200px;height:468px;background:linear-gradient(180deg,#fff 0%,var(--pale-blue) 45%,#fff 100%)}
.diet h2{position:absolute;left:613px;top:3722px;font-size:44px;color:#333;font-weight:500}
.pill{position:absolute;top:3945px;height:30px;line-height:30px;padding:0 16px;background:var(--green);color:#fff;font-size:12px}

/* testimonial */
.testimonial h2{position:absolute;left:80px;top:4144px;font-size:34px;color:var(--blue-dark)}
.quote{position:absolute;left:80px;top:4195px;width:491px;height:145px;border:2px solid #777;border-radius:10px;padding:18px 22px}
.quote p{font-size:13px;line-height:19px;color:#555}
.quote .who{margin-top:10px;font-size:12px;font-weight:600;color:#333}
.quote .role{font-size:11px;color:#777}

/* footer */
.footer{position:absolute;left:0;top:4452px;width:1200px;height:348px;background:var(--navy);color:#dde}
.footer h4{position:absolute;top:24px;font-family:'Raleway',sans-serif;font-weight:500;font-size:26px;color:#fff}
.event{position:absolute;left:80px;width:400px;height:86px}
.event .thumb{position:absolute;left:0;top:0;width:114px;height:86px;background:linear-gradient(135deg,#5a3b2a,#a0704e)}
.event p{position:absolute;left:130px;top:0;width:270px;font-size:12px;line-height:17px;color:#ccd}
.addr{position:absolute;left:532px;font-size:13px;color:#dde;display:flex;gap:10px;align-items:center}
.map{position:absolute;left:532px;top:168px;width:236px;height:106px;background:linear-gradient(135deg,#e8e4d8,#cfd8c4)}
.news-field{position:absolute;left:839px;width:281px;height:26px;background:#fff;font-size:11px;color:#999;line-height:26px;padding-left:8px}
.news-btn{position:absolute;left:839px;top:155px;width:80px;height:28px;background:var(--blue);color:#fff;font-size:13px;line-height:28px;text-align:center}
.sq{position:absolute;top:198px;width:30px;height:30px;border-radius:3px}
.copyright{position:absolute;left:0;top:4800px;width:1200px;height:39px;background:var(--green);color:#fff;font-size:12px;text-align:center;line-height:39px}
</style>
</head>
<body>

<nav class="nav">
  <div class="nav-item active" style="left:135px"><svg width="30" height="28" viewBox="0 0 30 28"><path d="M3 14 15 3l12 11M7 12v13h16V12" fill="none" stroke="#fff" stroke-width="3"/></svg>Home</div>
  <div class="nav-item" style="left:232px"><svg width="26" height="28"><circle cx="13" cy="10" r="7" fill="var(--green)"/><rect x="9" y="18" width="8" height="10" fill="var(--green)"/></svg>About</div>
  <div class="nav-item wide" style="left:371px"><svg width="26" height="28"><circle cx="13" cy="5" r="4" fill="var(--green)"/><path d="M13 9v10l-6 8M13 19l6 8M5 13h16" stroke="var(--green)" stroke-width="3" fill="none"/></svg>Work Out With Me</div>
  <div class="nav-item" style="left:516px"><svg width="26" height="28"><path d="M7 2v24M3 2v8h8V2M19 2c-4 4-4 10 0 12v12" stroke="var(--green)" stroke-width="3" fill="none"/></svg>Recipes</div>
  <div class="nav-item" style="left:636px"><svg width="26" height="28"><rect x="1" y="10" width="5" height="10" fill="var(--green)"/><rect x="20" y="10" width="5" height="10" fill="var(--green)"/><rect x="5" y="13" width="16" height="4" fill="var(--green)"/></svg>Fitness</div>
  <div class="nav-item" style="left:748px"><svg width="26" height="28"><circle cx="13" cy="9" r="7" fill="var(--green)"/><path d="M3 28c0-8 20-8 20 0" fill="var(--green)"/></svg>Sponsor</div>
  <div class="nav-item" style="left:852px"><svg width="26" height="28"><circle cx="8" cy="8" r="5" fill="var(--green)"/><circle cx="19" cy="10" r="4" fill="var(--green)"/><path d="M1 28c0-9 14-9 14 0M13 28c0-7 12-7 12 0" fill="var(--green)"/></svg>Family</div>
  <div class="nav-item" style="left:958px"><svg width="26" height="28"><circle cx="13" cy="14" r="11" fill="none" stroke="var(--green)" stroke-width="3"/><circle cx="9" cy="12" r="1.5" fill="var(--green)"/><circle cx="17" cy="12" r="1.5" fill="var(--green)"/><path d="M8 17c3 3 7 3 10 0" stroke="var(--green)" stroke-width="2" fill="none"/></svg>Friends</div>
  <div class="nav-item" style="left:1065px"><svg width="26" height="28"><rect x="2" y="5" width="22" height="21" fill="none" stroke="var(--green)" stroke-width="3"/><path d="M2 11h22M8 2v6M18 2v6" stroke="var(--green)" stroke-width="3"/></svg>Book</div>
</nav>

<header class="brand">
  <span class="brand-name"><i></i>FitNova</span>
</header>

<section class="subscribe">
  <div class="tag">Subscribe for famous Workouts Recipes and Fitness calendars</div>
  <label>Email Address<span style="color:var(--red)">*</span></label>
  <div class="field"></div>
  <div class="btn">Subscribe</div>
  <span class="social" style="left:905px"></span>
  <span class="social" style="left:950px"></span>
  <span class="social" style="left:995px"></span>
  <span class="social" style="left:1040px"></span>
  <span class="social" style="left:1085px"></span>
</section>
<div class="crowd" role="img" aria-label="Row of small colourful cartoon figures exercising"></div>

<section class="hero">
  <div class="ph" style="left:140px;top:20px;width:260px;height:520px;background:linear-gradient(180deg,rgba(40,25,15,.55),rgba(40,25,15,.35));" role="img" aria-label="Silhouette of a woman running on a beach at sunset"></div>
  <h1>Fitness Is Not A Destination<br>It Is A Way Of Life.</h1>
  <div class="cta">Sign Up Now</div>
</section>

<section class="fit">
  <h2>KEEP YOUR BODY FIT &amp; HEALTHY</h2>
  <p class="copy lead">Lorem ipsum dolor sit amet, consectetur adipiscing elit. Proin maximus, velit a imperdiet hendrerit, urna nulla placerat erat, in auctor odio arcu sit amet ante. Etiam lobortis, lacus imperdiet, odio tellus fermentum nisi, vel scelerisque massa magna nibh. Nulla sed justo enim pulvinar mattis.</p>
  <div class="card" style="left:80px" role="img" aria-label="Man lifting a dumbbell"><h3>Exercises</h3><p>Lorem ipsum dolor sit amet, consectetur adipiscing elit. Proin maximus, velit a imperdiet hendrerit urna nulla placerat erat.</p><span class="more">More Details</span></div>
  <div class="card" style="left:435px" role="img" aria-label="Hands holding a red heart"><h3>Improve Health &amp; Wellbeing</h3><p style="top:120px">Lorem ipsum dolor sit amet, consectetur adipiscing elit. Proin maximus velit.</p><span class="more">More Details</span></div>
  <div class="card" style="left:790px" role="img" aria-label="Close view of a toned torso"><h3>Weightloss</h3><p>Lorem ipsum dolor sit amet, consectetur adipiscing elit. Proin maximus, velit a imperdiet hendrerit urna nulla placerat erat.</p><span class="more">More Details</span></div>
</section>

<section class="feature">
  <div class="ph" style="left:80px;top:1680px;width:470px;height:450px;background:radial-gradient(ellipse at 50% 50%,#7a4a34 0%,#b0563e 35%,#fff 70%);" role="img" aria-label="Athlete in a sprint start pose"></div>
  <h2 style="left:613px;top:1638px">Customizable Workout Calendar</h2>
  <p class="copy" style="left:613px;top:1690px">Etiam a felis nec mi lobortis feugiat at eget erat. Nam ac ultrices eros. Morbi vitae egestas urna. Nam accumsan nec est ac bibendum. Sed faucibus leo sed ipsum ultricies vulputate. Duis convallis malesuada ultricies. Donec erat massa, pellentesque at nisl non, vestibulum egestas felis. Donec faucibus risus in metus suscipit blandit. Vivamus velit urna, faucibus eget quam eu, sagittis egestas est. Etiam sapien elit, vehicula vel aliquet a aliquam et nibh. Curabitur fermentum sed odio nec sollicitudin. Mauris pretium tempor quam sit amet blandit. Phasellus vel tristique erat. Quisque eu mattis sem.</p>
  <div class="calendar">
    <div class="title">2016 <span>MAY</span></div>
    <div class="ph" style="left:310px;top:20px;width:130px;height:70px;background:radial-gradient(circle,#b23a2e 0%,#7a9a3a 45%,transparent 70%)" role="img" aria-label="Cherries and a fresh fig"></div>
    <table>
      <tr><th>SUN</th><th>MON</th><th>TUE</th><th>WED</th><th>THURS</th><th>FRI</th><th>SAT</th></tr>
      <tr><td class="sun">1</td><td>2</td><td>3</td><td>4</td><td>5</td><td>6</td><td>7</td></tr>
      <tr><td class="sun">8</td><td>9</td><td>10</td><td>11</td><td>12</td><td>13</td><td>14</td></tr>
      <tr><td class="sun">15</td><td>16</td><td>17</td><td>18</td><td>19</td><td>20</td><td>21</td></tr>
      <tr><td class="sun">22</td><td>23</td><td>24</td><td>25</td><td>26</td><td>27</td><td>28</td></tr>
      <tr><td class="sun">29</td><td>30</td><td>31</td><td></td><td></td><td></td><td></td></tr>
    </table>
  </div>
</section>

<div class="progress-band"></div>
<section class="feature">
  <h2 style="left:80px;top:2312px">Progress Tracking</h2>
  <p class="copy" style="left:80px;top:2362px">Etiam a felis nec mi lobortis feugiat at eget erat. Nam ac ultrices eros. Morbi vitae egestas urna. Nam accumsan nec est ac bibendum. Sed faucibus leo sed ipsum ultricies vulputate. Duis convallis malesuada ultricies. Donec erat massa, pellentesque at nisl non, vestibulum egestas felis. Donec faucibus risus in metus suscipit blandit. Vivamus velit urna, faucibus eget quam eu, sagittis egestas est. Etiam sapien elit, vehicula vel aliquet a aliquam et nibh. Curabitur fermentum sed odio nec sollicitudin. Mauris pretium tempor quam sit amet blandit. Phasellus vel tristique erat. Quisque eu mattis sem.</p>
  <div class="ph" style="left:80px;top:2548px;width:470px;height:355px;background:linear-gradient(135deg,#fdf3f1 0%,#f6d8d2 55%,#f3d79a 100%)" role="img" aria-label="Hand-drawn rising chart on red grid paper with a pencil"></div>
  <div class="ph" style="left:677px;top:2297px;width:436px;height:623px;background:radial-gradient(ellipse at 50% 45%,#c89878 0%,#7a6a64 30%,transparent 62%)" role="img" aria-label="Woman in sportswear jumping mid-workout"></div>
</section>

<section class="feature">
  <div class="ph" style="left:177px;top:2975px;width:258px;height:622px;background:linear-gradient(180deg,#6b4a3a 0%,#9a6a4e 45%,#2f2f2f 75%,#d8d040 100%);border-radius:40% 40% 10% 10%" role="img" aria-label="Fit couple holding dumbbells"></div>
  <h2 style="left:613px;top:3005px">Daily Workout Programs</h2>
  <p class="copy" style="left:613px;top:3055px">Etiam a felis nec mi lobortis feugiat at eget erat. Nam ac ultrices eros. Morbi vitae egestas urna. Nam accumsan nec est ac bibendum. Sed faucibus leo sed ipsum ultricies vulputate. Duis convallis malesuada ultricies. Donec erat massa, pellentesque at nisl non, vestibulum egestas felis. Donec faucibus risus in metus suscipit blandit. Vivamus velit urna, faucibus eget quam eu, sagittis egestas est. Etiam sapien elit, vehicula vel aliquet a aliquam et nibh. Curabitur fermentum sed odio nec sollicitudin. Mauris pretium tempor quam sit amet blandit.</p>
  <div class="ph" style="left:613px;top:3226px;width:474px;height:362px;background:linear-gradient(135deg,#2f5a2a,#3d6e34)" role="img" aria-label="Chalkboard with four sticky notes reading good food, good workout, good rest, good health"></div>
</section>

<div class="diet-band"></div>
<section class="diet">
  <div class="ph" style="left:80px;top:3640px;width:485px;height:425px;background:radial-gradient(ellipse at 50% 60%,#f2f2ee 0%,#e08a5a 35%,#7aa04a 55%,transparent 75%)" role="img" aria-label="Glass of milk, salmon, eggs, spinach and beans"></div>
  <h2>Diet Plans</h2>
  <p class="copy" style="position:absolute;left:613px;top:3800px;width:500px">Lorem ipsum dolor sit amet, consectetur adipiscing elit. Quisque pretium lectus quam, non dapibus tellus sodales eu. Duis lorem urna, tempus sed mi vitae, sagittis auctor odio. Quisque nunc orci, varius vel sit, pharetra tristique nibh. Nullam commodo quam.</p>
  <p class="copy" style="position:absolute;left:613px;top:3890px;width:500px">Cras finibus pellentesque lorem, sed mollis ligula lobortis varius. Pellentesque et orci sem. Ut consectetur justo quis odio interdum efficitur.</p>
  <span class="pill" style="left:613px">For Men</span>
  <span class="pill" style="left:700px">For Women</span>
  <span class="pill" style="left:800px">More Details</span>
</section>

<section class="testimonial">
  <h2>TESTIMONIAL</h2>
  <svg class="abs" style="left:532px;top:4152px" width="40" height="20"><path d="M12 3 4 10l8 7M28 3l8 7-8 7" stroke="var(--blue)" stroke-width="3" fill="none"/></svg>
  <div class="quote">
    <p>Lorem ipsum dolor sit amet, consectetur adipiscing elit. Nulla fermentum dignissim risus eleifend sagittis. Integer lectus hendrerit a lorem leo, vestibulum bibendum. Nullam egestas mauris mi porta fenci nec lectus erat.</p>
    <div class="who">Sam Carter</div>
    <div class="role">Customer</div>
  </div>
  <div class="ph" style="left:597px;top:4226px;width:516px;height:226px;background:linear-gradient(90deg,#e9a85a,#5aa0d8,#d7d7d7,#f0c2a0,#7cc0e8)" role="img" aria-label="Group of smiling people of different ages in sportswear"></div>
</section>

<footer class="footer">
  <h4 style="left:80px">Event Information</h4>
  <div class="event" style="top:71px"><div class="thumb" role="img" aria-label="Bodybuilder flexing"></div><p>Lorem ipsum dolor sit amet consectetur elit.<br>Mauris euismod elit mi, et feugiat ante elementum ut. viverra vehicula velit non lacus. Pellentesque consequat hendrerit risus nec lacinia enim.</p></div>
  <div class="event" style="top:168px"><div class="thumb" role="img" aria-label="Athlete back muscles"></div><p>Lorem ipsum dolor sit amet consectetur elit.<br>Mauris euismod elit mi, et feugiat ante elementum ut. viverra vehicula velit non lacus. Pellentesque consequat hendrerit risus nec lacinia enim.</p></div>

  <h4 style="left:532px">Our Address</h4>
  <div class="addr" style="top:72px"><svg width="12" height="16"><path d="M6 16C1 9 0 7 0 6a6 6 0 0 1 12 0c0 1-1 3-6 10z" fill="#fff"/><circle cx="6" cy="6" r="2" fill="var(--navy)"/></svg><span>Unit 18, Maple Yard,<br>Leeds, United Kingdom</span></div>
  <div class="addr" style="top:118px"><svg width="14" height="14"><path d="M2 1h3l2 4-2 1c1 2 3 4 5 5l1-2 4 2v3c-7 1-14-6-13-13z" fill="#fff"/></svg><span style="font-size:16px;font-weight:600">0800 12 34 567</span></div>
  <div class="addr" style="top:146px"><svg width="14" height="10"><rect width="14" height="10" fill="#fff"/><path d="M0 0l7 6 7-6" stroke="var(--navy)" fill="none"/></svg><span>info@fitnova.com</span></div>
  <div class="map" role="img" aria-label="Street map of the studio location"></div>

  <h4 style="left:839px">Our Newsletter</h4>
  <div class="news-field" style="top:75px">Name</div>
  <div class="news-field" style="top:108px">Enter Your Email</div>
  <div class="news-btn">SIGN UP</div>
  <span class="sq" style="left:839px;background:#3b8fd6"></span>
  <span class="sq" style="left:875px;background:#d8262f"></span>
  <span class="sq" style="left:911px;background:#3b5998"></span>
  <span class="sq" style="left:947px;background:#1da1f2"></span>
  <span class="sq" style="left:983px;background:#e04030"></span>
  <span class="sq" style="left:1019px;background:#8cc63f"></span>
  <span class="sq" style="left:1055px;background:#1a8fc4"></span>
  <span class="sq" style="left:1091px;background:#3b8fd6"></span>
</footer>
<div class="copyright">Copyright 2016 @fitnova.com. All right are reserved</div>

</body>
</html>
```